Wine Label for a White and a Red Wine from Italy

We have a very good idea of what we want with artwork. We need you to please design a 'template' with the text so we can change out the artwork from year to year. Samples are shown of what we are looking for. We are looking for options with the two basic designs. Brand name of wine is: Valora del Torrino. Both wines are in a light green Bordeaux-style bottle (note: we don't show a light green bottle in the mockup but please remember the bottle is light green). Artwork is provided. We'd like to see either the green or blue butterfly on the white wine, the red butterfly is for the red wine. Please base the design on the attached label from Ashby and/or the attached label from Chateau Vellanges.

Target Market(s)

Millennials, women

Requirements
Must have
• The artwork (butterflies) attached.
Nice to have
• Elegant, readable fonts. Please make the text so it can be changed by the printer. Please make it so the artwork can be changed too.

```html
<!DOCTYPE html>
<html lang="en">
<head>
<meta charset="utf-8">
<title>Valora del Torrino — Barrel Select Labels</title>
<link rel="stylesheet" href="https://fonts.googleapis.com/css2?family=Kaushan+Script&family=Nunito+Sans:wght@300&family=Dosis:wght@400;500&display=swap">
<style>
  :root {
    --backdrop: #ecedf0;
    --label: #ffffff;
    --ink: #141414;
    --ink-soft: #2e2e33;
    --select-blue: #3d5b96;
    --wine-red: #a3284f;
  }
  * { box-sizing: border-box; margin: 0; padding: 0; }
  html, body {
    width: 1200px; height: 2199px; overflow: hidden;
    background: var(--backdrop);
  }
  .canvas { position: relative; width: 1200px; height: 2199px; }
  .label {
    position: absolute; top: 981px;
    width: 440px; height: 811px;
    background: var(--label);
    box-shadow: 0 6px 24px rgba(40, 45, 70, 0.12);
    text-align: center;
  }
  .label--red { left: 160px; }
  .label--white { left: 685px; }
  .label__brand {
    position: absolute; top: 38px; left: 0; right: 0;
    font-family: "Kaushan Script", cursive; font-weight: 400;
    color: var(--ink); line-height: 1;
  }
  .label__brand-main { display: block; font-size: 88px; }
  .label__brand-sub { display: block; font-size: 50px; margin-top: 4px; }
  .label__range {
    position: absolute; top: 246px; left: 0; right: 0;
    font-family: "Nunito Sans", sans-serif; font-weight: 300;
    font-size: 38px; line-height: 44px; letter-spacing: 0.5px;
    color: var(--select-blue);
  }
  .label__artwork {
    position: absolute; top: 303px; left: 0;
    width: 440px; height: 282px; display: block;
  }
  .label__vintage {
    position: absolute; top: 593px; left: 0; right: 0;
    font-family: "Dosis", sans-serif; font-weight: 500;
    font-size: 34px; line-height: 34px; color: var(--wine-red);
  }
  .label__origin {
    position: absolute; top: 629px; left: 0; right: 0;
    font-family: "Dosis", sans-serif; font-weight: 400;
    font-size: 23px; line-height: 27px; color: var(--wine-red);
  }
  .label__maker {
    position: absolute; top: 699px; left: 0; right: 0;
    font-family: "Dosis", sans-serif; font-weight: 400;
    font-size: 22px; line-height: 24px; color: var(--ink-soft);
  }
  .label__farming {
    position: absolute; top: 745px; left: 0; right: 0;
    font-family: "Dosis", sans-serif; font-weight: 400;
    font-size: 20px; line-height: 22px; color: var(--ink-soft);
  }
</style>
</head>
<body>
<main class="canvas">
  <section class="label label--red">
    <h1 class="label__brand"><span class="label__brand-main">Valora</span><span class="label__brand-sub">del Torrino</span></h1>
    <p class="label__range">BARREL SELECT</p>
    <svg class="label__artwork" viewBox="0 0 440 282" role="img" aria-label="Watercolour artwork of a butterfly among pink and violet flowers">
      <defs>
        <radialGradient id="artTonesRed" cx="50%" cy="50%" r="65%">
          <stop offset="0%" stop-color="#7f93d4"/>
          <stop offset="45%" stop-color="#c3a6da"/>
          <stop offset="80%" stop-color="#efbfd4"/>
          <stop offset="100%" stop-color="#f8e8f0"/>
        </radialGradient>
      </defs>
      <rect width="440" height="282" fill="url(#artTonesRed)"/>
    </svg>
    <p class="label__vintage">2018</p>
    <p class="label__origin">Rosso<br>Piemonte, Italy</p>
    <p class="label__maker">Artisanlly Crafted by Cantina Quattro Colli</p>
    <p class="label__farming">sustainably farmed</p>
  </section>

  <section class="label label--white">
    <h1 class="label__brand"><span class="label__brand-main">Valora</span><span class="label__brand-sub">del Torrino</span></h1>
    <p class="label__range">BARREL SELECT</p>
    <svg class="label__artwork" viewBox="0 0 440 282" role="img" aria-label="Watercolour artwork of a blue butterfly among pink and violet flowers">
      <defs>
        <radialGradient id="artTonesWhite" cx="50%" cy="50%" r="65%">
          <stop offset="0%" stop-color="#7f93d4"/>
          <stop offset="45%" stop-color="#c3a6da"/>
          <stop offset="80%" stop-color="#efbfd4"/>
          <stop offset="100%" stop-color="#f8e8f0"/>
        </radialGradient>
      </defs>
      <rect width="440" height="282" fill="url(#artTonesWhite)"/>
    </svg>
    <p class="label__vintage">2018</p>
    <p class="label__origin">Bianco<br>Piemonte, Italy</p>
    <p class="label__maker">Artisanlly Crafted by Cantina Quattro Colli</p>
    <p class="label__farming">sustainably farmed</p>
  </section>
</main>
</body>
</html>
```